Business Card Design Project

QPR Management Consulting, LLC is a management consulting firm focused on improving an organization’s health and wellness while enhancing company performance with an emphasis on winning in the marketplace, profitable growth, team building, culture enablement and innovation.

Industry/Entity Type

Business

```html
<!DOCTYPE html>
<html lang="en">
<head>
<meta charset="utf-8">
<title>QPR Management Consulting – Business Card</title>
<link href="https://fonts.googleapis.com/css2?family=Montserrat:wght@400;500;600&display=swap" rel="stylesheet">
<style>
  :root {
    --backdrop: #ebe7e1;
    --card: #222222;
    --ink-light: #ffffff;
    --ink-muted: #8c8c8c;
    --rule: #6e6e6e;
    --accent: #6cb33f;
  }
  * { box-sizing: border-box; margin: 0; padding: 0; }
  html, body {
    width: 1200px; height: 1165px; overflow: hidden;
    background: var(--backdrop);
    font-family: "Montserrat", Arial, sans-serif;
  }
  .card {
    position: absolute; left: 250px;
    width: 700px; height: 400px;
    background: var(--card);
    box-shadow: 0 8px 22px rgba(0,0,0,.25);
  }
  .card--front { top: 150px; }
  .card--back { top: 615px; }

  .brand-name {
    color: var(--ink-light);
    font-weight: 500;
    line-height: 1;
  }
  .brand-name .brand-short { display: block; font-size: 70px; letter-spacing: 1px; }
  .brand-name .brand-long { display: block; font-size: 24px; margin-top: 6px; letter-spacing: .5px; }

  .card--front .brand-name { position: absolute; left: 130px; top: 135px; }

  .card--back .brand-name { position: absolute; left: 60px; top: 50px; }
  .card--back .brand-name .brand-short { font-size: 52px; }
  .card--back .brand-name .brand-long { font-size: 18px; }

  .divider-top {
    position: absolute; left: 290px; right: 40px; top: 165px;
    border-top: 1px solid var(--rule);
  }
  .person { position: absolute; left: 70px; top: 190px; width: 590px; }
  .person-name { color: var(--ink-light); font-weight: 600; font-size: 30px; }
  .person-role {
    display: flex; align-items: center; gap: 8px;
    color: var(--ink-muted); font-size: 15px; margin-top: 4px;
  }
  .person-role::after { content: ""; flex: 1; border-top: 1px solid var(--rule); }

  .address {
    position: absolute; left: 75px; top: 300px;
    color: var(--ink-light); font-size: 17px; line-height: 1.5;
  }
  .contact {
    position: absolute; left: 420px; top: 272px;
    list-style: none; color: var(--ink-light); font-size: 16px; line-height: 1.6;
  }
  .contact li { display: flex; align-items: center; gap: 9px; }
  .contact svg { width: 15px; height: 15px; fill: var(--accent); flex: none; }
</style>
</head>
<body>
  <section class="card card--front">
    <div class="brand-name">
      <span class="brand-short">QPR</span>
      <span class="brand-long">Management Consulting, LLC</span>
    </div>
  </section>

  <section class="card card--back">
    <div class="brand-name">
      <span class="brand-short">QPR</span>
      <span class="brand-long">Management Consulting, LLC</span>
    </div>
    <div class="divider-top"></div>
    <div class="person">
      <p class="person-name">Daniel Reyes</p>
      <p class="person-role">Owner</p>
    </div>
    <address class="address" style="font-style:normal">
      48 Hollow Creek Lane<br>Millbrook, NC 28009
    </address>
    <ul class="contact">
      <li>
        <svg viewBox="0 0 16 16" aria-hidden="true"><path d="M2 6c0-2 2-3 6-3s6 1 6 3v1h-3V5.5H5V7H2z"/><path d="M4 8h8l2 6H2z"/></svg>
        1234-567-8910
      </li>
      <li>
        <svg viewBox="0 0 16 16" aria-hidden="true"><rect x="4" y="1" width="8" height="5"/><rect x="1" y="6" width="14" height="6" rx="1"/><rect x="4" y="11" width="8" height="4"/></svg>
        123-456-7890
      </li>
      <li>
        <svg viewBox="0 0 16 16" aria-hidden="true"><path d="M1 3h14v1L8 9 1 4z"/><path d="M1 5.5l7 5 7-5V13H1z"/></svg>
        yourname@yoursite.com
      </li>
      <li>
        <svg viewBox="0 0 16 16" aria-hidden="true"><path d="M8 1a7 7 0 1 0 0 14A7 7 0 0 0 8 1zm0 1.5c.9 0 1.8 1.5 2.1 4H5.9C6.2 4 7.1 2.5 8 2.5zM2.6 7.5h2.3a12 12 0 0 0 0 1H2.6zm0 1h2.3c.1 1 .3 2 .6 2.8A5.5 5.5 0 0 1 2.6 8.5zM5.9 8.5h4.2c-.3 2.5-1.2 4-2.1 4s-1.8-1.5-2.1-4zm5.2 0h2.3a5.5 5.5 0 0 1-2.9 3.8c.3-.9.5-1.9.6-2.8zm0-1c-.1-1-.3-2-.6-2.8a5.5 5.5 0 0 1 2.9 3.8z"/></svg>
        www.yoursite.com
      </li>
    </ul>
  </section>
</body>
</html>
```